Business Card Design

We need a business card design for a kids clothes shop in Ireland called "Tiny Trotz". Would prefer the colours Lime Green and Dark Purple to be used but are open to suggestions. The logo should include a "Cool" penguin with clothes on.

Industry/Entity Type

Shop

Contact Information for Business Card

Tiny Trotz
Harlow Arcade,
Ashvale Road, Childrenswear 0-12yrs
Kilbarrow,
XQ82 5LW. Deirdre Walsh.

```html
<!DOCTYPE html>
<html lang="en">
<head>
<meta charset="utf-8">
<title>Tiny Trotz – Business Card</title>
<link rel="stylesheet" href="https://fonts.googleapis.com/css2?family=Open+Sans:wght@300;400&display=swap">
<style>
  :root {
    --card-bg: #323232;
    --lime: #8dc63f;
    --soft-grey: #9a9a9a;
    --mid-grey: #7d7d7d;
  }
  html, body {
    margin: 0;
    padding: 0;
    width: 1200px;
    height: 791px;
    overflow: hidden;
    background: var(--card-bg);
  }
  .card {
    position: relative;
    width: 1200px;
    height: 791px;
    background: var(--card-bg);
    font-family: "Open Sans", Arial, sans-serif;
  }
  .contact {
    position: absolute;
    right: 121px;
    top: 114px;
    text-align: right;
  }
  .contact__name {
    margin: 0;
    font-size: 54px;
    font-weight: 300;
    line-height: 1;
    letter-spacing: 0.5px;
  }
  .contact__first { color: var(--lime); font-weight: 400; }
  .contact__last { color: var(--soft-grey); }
  .contact__address {
    margin: 32px 0 0;
    font-size: 22px;
    font-weight: 300;
    line-height: 28px;
    color: var(--soft-grey);
    font-style: normal;
  }
  .brand {
    position: absolute;
    left: 58px;
    top: 589px;
    display: flex;
    align-items: flex-start;
  }
  .brand__dot {
    width: 138px;
    height: 138px;
    flex: none;
  }
  .brand__text { margin-left: 37px; padding-top: 46px; }
  .brand__name {
    margin: 0;
    font-size: 42px;
    font-weight: 300;
    line-height: 1;
    color: var(--lime);
  }
  .brand__tagline {
    margin: 6px 0 0;
    font-size: 16px;
    font-weight: 300;
    color: var(--mid-grey);
  }
</style>
</head>
<body>
  <main class="card">
    <section class="contact">
      <h1 class="contact__name"><span class="contact__first">Deirdre</span><span class="contact__last">Walsh</span></h1>
      <address class="contact__address">
        Harlow Arcade , Ashvale Road<br>
        Kilbarrow , XQ82 5LW
      </address>
    </section>

    <section class="brand">
      <svg class="brand__dot" viewBox="0 0 138 138" aria-hidden="true">
        <circle cx="69" cy="69" r="69" fill="#8dc63f"/>
      </svg>
      <div class="brand__text">
        <p class="brand__name">Tiny Trotz</p>
        <p class="brand__tagline">Childrenswear | 0-12yrs</p>
      </div>
    </section>
  </main>
</body>
</html>
```